" Atendemos de maneira integrada em reabilitação ,tanto odontológica como neurológica. Somos terapia ocupacional, fonoaudiologia, neuropediatria e odontologia. Trabalhamos com técnicas de ponta e muito proximidade com nossos pacientes e suas famílias. "

```html
<!DOCTYPE html>
<html lang="pt-BR">
<head>
<meta charset="utf-8">
<title>Nexo Vital – Cartão de visita</title>
<link href="https://fonts.googleapis.com/css2?family=Montserrat:wght@400;500;700&display=swap" rel="stylesheet">
<style>
  :root {
    --bg: #eceae6;
    --card-white: #ffffff;
    --navy: #1f4468;
    --navy-deep: #193a5a;
    --brand-blue: #2b5580;
    --accent-green: #8cc56a;
    --text-light: #e9eef4;
  }
  * { margin: 0; padding: 0; box-sizing: border-box; }
  html, body { width: 1200px; height: 1200px; overflow: hidden; }
  body {
    background: var(--bg);
    font-family: "Montserrat", sans-serif;
    position: relative;
  }
  .card {
    position: absolute;
    left: 200px;
    width: 800px;
    height: 445px;
    border-radius: 48px;
    box-shadow: 0 12px 30px rgba(0,0,0,0.12);
    overflow: hidden;
  }
  .card--front { top: 110px; background: var(--card-white); }
  .card--back {
    top: 645px;
    background: linear-gradient(160deg, var(--navy) 0%, var(--navy-deep) 100%);
    color: var(--text-light);
  }

  .brand {
    position: absolute;
    left: 0; right: 0; top: 130px;
    display: flex; flex-direction: column; align-items: center;
  }
  .brand__mark {
    width: 70px; height: 70px; border-radius: 50%;
    background: var(--accent-green);
    margin-bottom: 24px;
  }
  .brand__name {
    font-weight: 700; font-size: 64px; letter-spacing: 3px;
    color: var(--brand-blue); line-height: 1;
  }
  .brand__partners {
    margin-top: 8px;
    font-weight: 400; font-size: 22px; color: var(--brand-blue);
  }

  .back__decor {
    position: absolute; left: 70px; top: 60px;
    width: 300px; height: 300px; border-radius: 50%;
    background: rgba(255,255,255,0.05);
  }
  .back__edge {
    position: absolute; right: 0; top: 110px;
    width: 14px; height: 220px;
    background: var(--accent-green);
  }
  .person {
    position: absolute; right: 70px; top: 70px; text-align: right;
  }
  .person__name { font-size: 30px; font-weight: 500; }
  .person__role { font-size: 26px; font-weight: 400; margin-top: 2px; }
  .contacts {
    position: absolute; right: 44px; top: 200px;
    list-style: none; text-align: right;
    font-size: 20px; line-height: 30px;
  }
  .contacts li { display: flex; justify-content: flex-end; align-items: center; gap: 12px; }
  .contacts svg { width: 16px; height: 16px; fill: var(--text-light); flex: none; }
  .contacts .no-icon { padding-right: 28px; }
</style>
</head>
<body>
  <section class="card card--front">
    <div class="brand">
      <span class="brand__mark"></span>
      <span class="brand__name">NEXO VITAL</span>
      <span class="brand__partners">Paulo Andrade &amp; Helena Sarmento</span>
    </div>
  </section>

  <section class="card card--back">
    <div class="back__decor"></div>
    <div class="back__edge"></div>
    <div class="person">
      <p class="person__name">Nome Sobrenome</p>
      <p class="person__role">função</p>
    </div>
    <ul class="contacts">
      <li>nexovital <svg viewBox="0 0 16 16"><circle cx="8" cy="8" r="6"/></svg></li>
      <li>contato@nexovital.com <svg viewBox="0 0 16 16"><rect x="1" y="3" width="14" height="10" rx="1"/></svg></li>
      <li>(00)0000-0000 <svg viewBox="0 0 16 16"><path d="M4 1l3 3-2 2c1 2 3 4 5 5l2-2 3 3-2 3C7 15 1 9 1 3z"/></svg></li>
      <li>rua sem nome,00 Bairro Sem Nome <svg viewBox="0 0 16 16"><path d="M8 0a5.5 5.5 0 0 0-5.5 5.5C2.5 10 8 16 8 16s5.5-6 5.5-10.5A5.5 5.5 0 0 0 8 0zm0 8a2.5 2.5 0 1 1 0-5 2.5 2.5 0 0 1 0 5z"/></svg></li>
      <li class="no-icon">Cidade Sem Nome</li>
    </ul>
  </section>
</body>
</html>
```